Multi-Faceted Legal and Finanacial Advisory Group Needs Business Card Design

We need a business card design for a newly branded Orlando Florida area advising group consisting of Attorneys, Accountants and Financial Planners. The company is named TK Counsel Partners. You will find our initial work on a business card. The information on the business card are merely guideposts and not final product. The logo does not have the be the same as provided since we have not finalized the logo. We would like to stay with a black/white/grey color scheme, but limited use of color is not out of the question.

Target Market(s)

Businesses and their Corporate Representatives

Industry/Entity Type

Business

Contact Information for Business Card

Should have Name, Title, Phone, Cell, Fax, Email and website. Logo should incorporate TK in some fashion however final logo used does not have to be the one on the document provided.

Requirements
Must have
• An TK design on front and back.

```html
<!DOCTYPE html>
<html lang="en">
<head>
<meta charset="utf-8">
<title>TK Counsel Partners – Business Card</title>
<link href="https://fonts.googleapis.com/css2?family=Questrial&display=swap" rel="stylesheet">
<style>
  :root {
    --backdrop: #4b4039;
    --card: #141414;
    --card-edge: #1c1c1c;
    --silver: #a9a9a9;
    --silver-light: #d6d6d6;
    --white: #f2f2f2;
    --muted: #7d7d7d;
    --rule: #8a8a8a;
  }
  * { margin: 0; padding: 0; box-sizing: border-box; }
  html, body {
    width: 1200px; height: 716px; overflow: hidden;
    background: var(--backdrop);
    font-family: "Questrial", "Century Gothic", sans-serif;
  }
  .sheet {
    position: relative; width: 1200px; height: 716px;
    display: flex; align-items: center; justify-content: center; gap: 40px;
  }
  .card {
    position: relative; width: 540px; height: 310px;
    background: linear-gradient(135deg, var(--card-edge), var(--card));
    box-shadow: 0 10px 26px rgba(0,0,0,.45);
    color: var(--white);
  }

  /* Front */
  .card--front {
    display: flex; flex-direction: column; align-items: center; justify-content: center;
  }
  .brand-mark {
    display: flex; flex-direction: column; align-items: center; gap: 12px;
  }
  .brand-square {
    width: 78px; height: 78px;
    background: linear-gradient(135deg, var(--silver-light), #6f6f6f);
  }
  .brand-name {
    font-size: 17px; letter-spacing: 2px; text-transform: uppercase; color: var(--silver-light);
  }
  .services {
    margin-top: 18px; font-size: 14px; color: var(--silver-light); letter-spacing: .5px;
  }
  .services .dot { margin: 0 6px; }
  .rule-row {
    margin-top: 12px; display: flex; align-items: center; gap: 14px;
  }
  .rule-row .rule { width: 70px; height: 1px; background: var(--rule); }
  .website { font-size: 14px; color: var(--white); letter-spacing: .5px; }

  /* Back */
  .card--back { padding: 34px 36px; display: flex; gap: 34px; }
  .back-brand {
    width: 150px; display: flex; flex-direction: column; gap: 10px;
    border-right: 1px solid var(--rule); padding-right: 20px;
  }
  .back-brand .brand-square { width: 96px; height: 96px; }
  .back-brand .brand-name { font-size: 13px; letter-spacing: 1.5px; color: var(--white); }
  .details { flex: 1; display: flex; flex-direction: column; }
  .person-name { font-size: 17px; letter-spacing: 1px; color: var(--muted); text-transform: uppercase; }
  .person-title { font-size: 14px; color: var(--white); margin-top: 2px; }
  .contact-list { list-style: none; margin-top: 20px; display: flex; flex-direction: column; gap: 5px; }
  .contact-list li { display: flex; align-items: center; gap: 9px; font-size: 13px; color: var(--white); }
  .contact-list svg { width: 13px; height: 13px; flex: none; }
  .address { margin-top: 14px; font-size: 13px; line-height: 1.45; color: var(--white); }
  .back-rule { margin-top: auto; height: 1px; background: var(--rule); }
</style>
</head>
<body>
<main class="sheet">

  <section class="card card--front" aria-label="Card front">
    <div class="brand-mark">
      <div class="brand-square"></div>
      <div class="brand-name">TK Counsel Partners</div>
    </div>
    <p class="services">Attorneys<span class="dot">•</span>Accountants<span class="dot">•</span>Financial Planners</p>
    <div class="rule-row">
      <span class="rule"></span>
      <span class="website">www.tk-counsel.com</span>
      <span class="rule"></span>
    </div>
  </section>

  <section class="card card--back" aria-label="Card back">
    <div class="back-brand">
      <div class="brand-square"></div>
      <div class="brand-name">TK Counsel Partners</div>
    </div>
    <div class="details">
      <p class="person-name">Daniel R. Marlow, Esq.</p>
      <p class="person-title">Attorney</p>
      <ul class="contact-list">
        <li>
          <svg viewBox="0 0 16 16"><rect width="16" height="16" rx="2" fill="#f2f2f2"/><path d="M5 3.5l2 2.5-1.2 1.2a7 7 0 0 0 3 3L10 9l2.5 2-1.2 1.5C7.5 12.3 3.7 8.5 3.5 4.7z" fill="#141414"/></svg>
          (555) 014-2231
        </li>
        <li>
          <svg viewBox="0 0 16 16"><rect x="4" y="1" width="8" height="14" rx="1.5" fill="none" stroke="#f2f2f2" stroke-width="1.6"/><circle cx="8" cy="12.5" r="0.9" fill="#f2f2f2"/></svg>
          (555) 014-2290
        </li>
        <li>
          <svg viewBox="0 0 16 16"><rect x="4" y="1" width="8" height="5" fill="#f2f2f2"/><rect x="1" y="6" width="14" height="7" rx="1" fill="#f2f2f2"/><rect x="4" y="10" width="8" height="5" fill="#141414" stroke="#f2f2f2"/></svg>
          (555) 014-2245
        </li>
        <li>
          <svg viewBox="0 0 16 16"><rect x="1" y="3" width="14" height="10" rx="1" fill="#f2f2f2"/><path d="M1.5 3.8L8 9l6.5-5.2" fill="none" stroke="#141414" stroke-width="1.4"/></svg>
          dmarlow@tk-counsel.com
        </li>
        <li>
          <svg viewBox="0 0 16 16" fill="none" stroke="#f2f2f2" stroke-width="1.3"><circle cx="8" cy="8" r="6.5"/><ellipse cx="8" cy="8" rx="3" ry="6.5"/><path d="M1.5 8h13M2.5 4.8h11M2.5 11.2h11"/></svg>
          www.tk-counsel.com
        </li>
      </ul>
      <p class="address">2200 Harbor Crest Drive,<br>Suite 410 Cedar Glen, FL 32799</p>
      <div class="back-rule"></div>
    </div>
  </section>

</main>
</body>
</html>
```